PLUM- company with a mission

PLUM LLC stands for pure living under moonlight (non profit arm is called bright lantern foundation)—our business is based out of New York City and has a non-profit arm where for every bar you purchase, we donate a bar (don’t want any designs that limits us to only soap). Currently working with South Africa. We want the focus to be organic/natural soap with a mission.
What our website needs to…achieve:
Purpose = branding, building up interesting leaving up to launch date, then a full functional site for selling soap (for now) with a mission. With that said, there will need to be a page designed for “COMING SOON” – with a place to post our teaser 30 second video (kind of like a commercial/movie trailer) – until everything else is done.
We are the first in the industry to do one for one (or …50/50). Most companies that do charity work are mostly for every $$$ we donate $0.10, or 1% of XXX. We are starting out to run the non-profit arm as well not just after we reach certain milestones. In addition, we will be transparent for the non-profit side whereas most of the time when you donate, you have no idea where the money ends up going.
IN ADDITION: we still need to be clean/elegant – and selling our soap; so website will need to 1. Showcase our products, 2. Be very clear that we have a mission (not sure if there is a way to show case both our soap AND our mission)
Some sites we like:
Velbrook.com—like them in terms of business model—in terms of their website: like how their site is clean and friendly, but it seems too cluttered
www.quindelmarsh.com -- similar business model, www.pemaroux.com, kelvashop.com, ridgelybar.com
Duvik.com: like this a lot better than fernwicke.com, however, major dislike of the typeface. Okay about the neutral colors…although feel like we need something a bit more cheerful here and there for our mission
Zlabel.net, kelvashop.com, castlewren.com: like how they are clean and showcase well
**** However, our site also needs to convey messages like: www.feverfreeworld.org, www.cleanhandsunited.org
Looking for a clean, simple design. Modern, clutter-free, and inviting. Definitely do not want an arts and crafty/flowery feel. We do need something…cheerful for our nonprofit purposes.
Examples of sites we don’t like: marigoldhaus.com, petalpressbar.com
7 pages/ tabs maybe? (About us…video page (to show case what we are doing –currently my partner is in South Africa filming what our mission will be able to do – give children and those in need soap), FAQs, soap products, terms & conditions, contact us page, blog page……nothing too crazy).
For now, for designing purposes, please use any example texts whether it’s the about us page, mission page..policies.. and for the soap/products pages—please use example you can find online – it is fine, we just need the design done for now.
I have also attached our logo file. Please let me know if you have any questions! Thanks!
Something to consider....
velbrook.com and quindelmarsh.com are probably our largest competitor out of all the websites I mentioned as they have a very similar business model where it is is a company with a mission. Homepage makes that clear that for every pair of shoes/ glasses you purchase, they give a pair. Another thing to note...is that they have been in business for a few years so their website probably have changed to more commercial than focusing/marketing on the mission of doing good. While we don't want that to be the total focus, we do need it to be present on the homepage/front page.
Non-Profit

```html
<!DOCTYPE html>
<html lang="en">
<head>
<meta charset="utf-8">
<title>PLUM — Soap with a mission</title>
<link rel="stylesheet" href="https://fonts.googleapis.com/css2?family=Open+Sans:wght@400;600;700;800&display=swap">
<style>
:root{
  --orange:#f3ab68;
  --ink:#333333;
  --topbar:#2b2b2b;
  --footer:#1d1d1d;
  --footer-base:#111111;
  --muted:#9a9a9a;
  --white:#ffffff;
  --rule:#d6d6d6;
}
*{margin:0;padding:0;box-sizing:border-box}
html,body{width:697px;height:1200px;overflow:hidden;background:var(--white)}
body{font-family:"Open Sans",Arial,sans-serif;color:var(--ink);position:relative}
.abs{position:absolute}

.topbar{left:0;top:0;width:697px;height:27px;background:var(--topbar)}
.topbar-links{right:59px;top:0;height:27px;display:flex;align-items:center;gap:14px;color:var(--white);font-size:8px}
.basket{display:flex;align-items:center;gap:5px}

.mainnav{left:0;top:27px;width:697px;height:48px;background:var(--white)}
.brand{left:58px;top:7px;width:62px;height:62px;border-radius:50%;background:var(--orange);display:flex;align-items:center;justify-content:center;color:var(--white);font-weight:700;font-size:17px;letter-spacing:1px;z-index:2}
.nav-list{right:56px;top:44px;display:flex;list-style:none;font-size:8px;color:#444}
.nav-list li{padding:0 9px;border-left:1px solid #cfcfcf;line-height:15px}
.nav-list li:first-child{border-left:none}

.hero{left:0;top:75px;width:697px;height:290px;background:linear-gradient(120deg,#c9d5e4 0%,#e8c6b2 45%,#d9a890 60%,#aebfd6 100%)}
.hero-panel{left:57px;top:170px;width:265px;height:99px;background:rgba(90,90,90,.55);color:var(--white);padding:18px 0 0 20px}
.hero-title{font-size:21px;font-weight:400;line-height:22px}
.hero-text{font-size:7.5px;line-height:9px;margin-top:1px}
.btn-orange{display:inline-block;margin-top:11px;background:var(--orange);color:var(--white);font-size:7.5px;padding:5px 9px}
.hero-dots{left:58px;top:339px;display:flex;gap:8px}
.hero-dots span{width:5px;height:5px;background:var(--white)}
.hero-dots span:first-child{background:var(--orange)}

.mission{left:0;top:394px;width:697px;text-align:center}
.mission h1{font-size:14px;font-weight:400;color:#333}
.mission h1 b{font-weight:700}
.mission p{width:504px;margin:7px auto 0;font-size:7.5px;line-height:8.7px;color:#555}
.divider{left:86px;top:477px;width:525px;height:1px;background:var(--rule)}

.product{top:510px;width:167px;height:197px}
.product-photo{width:167px;height:169px}
.product-label{height:28px;background:var(--orange);color:var(--white);font-size:7.5px;line-height:9px;padding:5px 8px 0 9px;display:flex;justify-content:space-between}
.product-label .price{padding-top:4px}

.pledge{left:77px;top:730px;width:544px;height:209px}
.pledge-photo{left:0;top:0;width:409px;height:209px;background:radial-gradient(ellipse at 40% 45%,#b79c78 0%,#8d8a84 35%,#5a5a58 75%,#3e3e3e 100%)}
.pledge-card{left:409px;top:0;width:135px;height:209px;background:var(--orange);color:var(--white);font-weight:800;text-transform:uppercase;padding:30px 0 0 13px;line-height:.95}
.pledge-card .lg{font-size:20px;display:block}
.pledge-card .md{font-size:14.5px;display:block}
.btn-dark{left:400px;top:152px;width:93px;height:24px;background:#1e1e1e;color:var(--white);font-size:10px;font-weight:700;display:flex;align-items:center;justify-content:center}

.footer{left:0;top:980px;width:697px;height:190px;background:var(--footer)}
.footer-col{top:24px}
.footer-col h2{font-size:9px;font-weight:700;color:var(--orange);margin-bottom:6px}
.footer-col ul{list-style:none;font-size:6.6px;line-height:7.9px;color:var(--muted);text-transform:uppercase}
.social{display:flex;gap:8px;margin-top:3px}
.social span{width:18px;height:18px;border-radius:50%;background:var(--white)}
.payments{left:526px;top:150px;display:flex;gap:3px}
.payments span{width:20px;height:11px;border-radius:1px}
.base{left:0;top:1170px;width:697px;height:30px;background:var(--footer-base)}
.copyright{right:76px;top:10px;font-size:6.6px;color:var(--muted)}
</style>
</head>
<body>

<header>
  <div class="abs topbar">
    <nav class="abs topbar-links">
      <span>HELP</span><span>LOG IN</span>
      <span class="basket">
        <svg width="12" height="10" viewBox="0 0 12 10"><path d="M1 3h10l-1.5 6h-7z" fill="none" stroke="#fff" stroke-width="1.2"/><path d="M3.5 3 5 0.8M8.5 3 7 0.8" stroke="#fff" stroke-width="1"/></svg>
        BASKET (0)
      </span>
    </nav>
  </div>
  <div class="abs mainnav">
    <ul class="abs nav-list" style="top:17px">
      <li>ABOUT US</li><li>OUR MISSION</li><li>FAQ</li><li>SOAP PRODUCTS</li><li>TERMS &amp; CONDITIONS</li><li>CONTACT US</li><li>BLOG PAGE</li>
    </ul>
  </div>
  <div class="abs brand">PLUM</div>
</header>

<section class="abs hero" role="img" aria-label="Photo of many hands stacked together in a team gesture"></section>
<div class="abs hero-panel">
  <div class="hero-title">SOAP SAVES LIVES</div>
  <div class="hero-text">Sed tortor diam, condimentum non ligula Duis semper vestibulum<br>Donec quis rhoncus tortor, vel scelerisque quam.</div>
  <span class="btn-orange">KNOW MORE</span>
</div>
<div class="abs hero-dots"><span></span><span></span><span></span><span></span></div>

<section class="abs mission">
  <h1>WE’RE BUILDING A COMPANY TO DO <b>GOOD IN THE WORLD</b></h1>
  <p>Nulla pharetra metus et rutrum aliquet. Aliquam eget magna consequat, consequat sapien eget, vestibulum ipsum. Sed massa ligula, sceleris­que eget lobortis nec, blandit eu nisi. Aliquam viverra euismod ligula eu accumsan. Suspendisse imperdiet lorem vel nulla adipiscing, vel eleif­end velit condimentum. Donec fermentum ligula massa.</p>
</section>
<div class="abs divider"></div>

<article class="abs product" style="left:77px">
  <div class="product-photo" role="img" aria-label="Wrapped pink soap bars with printed labels" style="background:linear-gradient(135deg,#f3efe9,#ead2c3 60%,#f2e8dc)"></div>
  <div class="product-label"><span>HARBOR LANE hand cream<br>Ridgely Co.</span><span class="price">$24.00</span></div>
</article>
<article class="abs product" style="left:266px">
  <div class="product-photo" role="img" aria-label="Boxed soaps in bright pink and blue packaging" style="background:linear-gradient(135deg,#eef1f5,#d98bb0 45%,#5a86c8 70%,#e9eef4)"></div>
  <div class="product-label"><span>HARBOR LANE hand cream<br>Ridgely Co.</span><span class="price">$24.00</span></div>
</article>
<article class="abs product" style="left:454px">
  <div class="product-photo" role="img" aria-label="Handmade lavender soap bar on a wooden table beside a kraft paper parcel" style="background:linear-gradient(160deg,#2a2622,#8a7a62 45%,#d9ceb0 65%,#5b5046)"></div>
  <div class="product-label"><span>HARBOR LANE hand cream<br>Ridgely Co.</span><span class="price">$24.00</span></div>
</article>

<section class="abs pledge">
  <div class="abs pledge-photo" role="img" aria-label="Hands holding a cardboard donation box"></div>
  <div class="abs pledge-card">
    <span class="md" style="font-size:16px">With every</span>
    <span class="lg">Product</span>
    <span class="md">You purchase</span>
    <span class="md">we will help</span>
    <span class="lg">a person</span>
    <span class="md">in need.</span>
  </div>
  <div class="abs btn-dark">KNOW MORE</div>
</section>

<footer>
  <div class="abs footer">
    <div class="abs footer-col" style="left:76px">
      <h2>ABOUT PLUM</h2>
      <ul><li>Rowan Ellery’s Bio</li><li>Company Information</li><li>Corporate Responsibility</li><li>Jobs at Velbrook</li><li>Affiliate Program</li><li>Request a Catalog</li></ul>
    </div>
    <div class="abs footer-col" style="left:199px">
      <h2>GET HELP</h2>
      <ul><li>Track my Order</li><li>Returns</li><li>Contact Information</li><li>Questions</li><li>Call us: 0000000000</li></ul>
    </div>
    <div class="abs footer-col" style="left:315px">
      <h2>FAN FAVORITES</h2>
      <ul><li>Sandals</li><li>Sunglasses for Men</li><li>Sunglasses for Women</li><li>Lace up Shoes</li><li>Kids’ Shoes</li><li>Velbrook Gift Cards</li><li>Marketplace</li><li>Coffee</li></ul>
    </div>
    <div class="abs footer-col" style="left:525px">
      <h2>FIND US ON</h2>
      <div class="social" aria-label="Social links"><span></span><span></span><span></span><span></span></div>
    </div>
    <div class="abs payments" aria-label="Accepted payment methods">
      <span style="background:#3b6fb6"></span><span style="background:#2f5fa8"></span><span style="background:#f2f2f2"></span><span style="background:#1f4aa0"></span>
    </div>
  </div>
  <div class="abs base">
    <div class="abs copyright">COPYRIGHT 2014 © PLUM LLC | &nbsp;ALL RIGHTS RESERVED. PRIVACY POLICY</div>
  </div>
</footer>

</body>
</html>
```